Public Speaking Book for aspiring, ambitious speakers

I'm looking for a 6x9 book cover (Brevora standard) as well as ebook and audiobook formats.

I'm looking for orange font on a white background as these are my brand colours.

Feel free to use some yellow and gold too if you deem it appropriate.

Title: Climb and Kindle
Subtitle: Find Your Voice. Tell Your Story. Share your Message.
Author: Tobias Wenlock

I would like to have a picture of a female speaker on the front cover.

Alternatively, some kind of image that symbolises public speaking like a microphone, podium etc

Target Market(s)

Aspiring professional speakers

Colors
f78f20

Requirements
Must have
• Correct spelling!
Nice to have
• A logo or picture that fits the theme, but no pressure if you can't think of anything
Should not have
• No men in suits please. I don't want this to have a 1980s corporate look.

```html
<!DOCTYPE html>
<html lang="en">
<head>
<meta charset="utf-8">
<title>Climb and Kindle — Tobias Wenlock</title>
<link rel="stylesheet" href="https://fonts.googleapis.com/css2?family=Marcellus&display=swap">
<style>
  :root {
    --brand-orange: #f78f20;
    --cover-white: #ffffff;
    --tagline-gold: #8c7a14;
    --author-bronze: #6e5a1c;
    --mic-steel: #5f5f5f;
    --mic-gold: #b39a4c;
  }
  * { margin: 0; padding: 0; box-sizing: border-box; }
  html, body {
    width: 1090px;
    height: 1200px;
    overflow: hidden;
    background: var(--brand-orange);
  }
  .cover {
    position: absolute;
    left: 165px;
    top: 30px;
    width: 760px;
    height: 1140px;
    background: var(--cover-white);
    font-family: "Marcellus", serif;
    overflow: hidden;
  }
  .cover > * {
    position: absolute;
    left: 0;
    width: 100%;
    text-align: center;
  }
  .author {
    top: 50px;
    font-size: 24px;
    line-height: 34px;
    letter-spacing: 0.62em;
    padding-left: 0.62em;
    color: var(--author-bronze);
  }
  .title-word {
    color: var(--brand-orange);
    font-weight: 400;
  }
  .title-climb {
    top: 140px;
    font-size: 200px;
    line-height: 180px;
    letter-spacing: -0.01em;
  }
  .speaker-figure {
    display: inline-block;
    width: 36px;
    height: 190px;
    margin: 0 4px;
    vertical-align: -22px;
    border-radius: 18px 18px 8px 8px;
    background: linear-gradient(180deg, var(--brand-orange), #f59a3a);
  }
  .visually-hidden {
    position: absolute;
    width: 1px;
    height: 1px;
    overflow: hidden;
    clip: rect(0 0 0 0);
  }
  .title-and {
    top: 392px;
    font-size: 118px;
    line-height: 116px;
  }
  .title-kindle {
    top: 583px;
    font-size: 118px;
    line-height: 116px;
  }
  .tagline {
    font-size: 31px;
    line-height: 40px;
    color: var(--tagline-gold);
  }
  .tagline-voice { top: 348px; }
  .tagline-story { top: 526px; }
  .tagline-message { top: 704px; }
  .microphone {
    top: 764px;
    left: 242px;
    width: 282px;
    height: 376px;
    border-radius: 120px 120px 0 0 / 70px 70px 0 0;
    background: linear-gradient(180deg, var(--mic-steel) 0%, #8a8a8a 40%, var(--mic-gold) 62%, #8d7a3c 100%);
  }
</style>
</head>
<body>
  <main class="cover">
    <p class="author">TOBIAS WENLOCK</p>

    <h1 class="title-word title-climb" aria-label="Climb">CL<span class="speaker-figure" role="img" aria-label="Silhouette of a woman speaker standing in place of the letter I"></span><span class="visually-hidden">I</span>MB</h1>
    <p class="tagline tagline-voice">FIND YOUR VOICE.</p>

    <p class="title-word title-and">AND</p>
    <p class="tagline tagline-story">TELL YOUR STORY.</p>

    <p class="title-word title-kindle">KINDLE</p>
    <p class="tagline tagline-message">SHARE YOUR MESSAGE.</p>

    <div class="microphone" role="img" aria-label="Photograph of a silver and gold stage microphone head"></div>
  </main>
</body>
</html>
```